R & T Summit Construction Business Card ideas

We want a business card to represents our company in a way that looks professional but is also a business card that is unique!

Industry/Entity Type

Construction Company

Contact Information for Business Card

open to all design ideas, just want to be able to see different options to choose from in either color or grayscale.

Requirements
Must have
• Our names and phone numbers
• Nolan Pritchett 512-804-2271
• Curtis Hale 512-693-1804
• Business logo

```html
<!DOCTYPE html>
<html lang="en">
<head>
<meta charset="utf-8">
<title>R &amp; T Summit Construction – Business Cards</title>
<link rel="stylesheet" href="https://fonts.googleapis.com/css2?family=Open+Sans:wght@400;600;700&display=swap">
<style>
  :root {
    --canvas-bg: #e9e7e4;
    --card-white: #ffffff;
    --card-black: #000000;
    --ink: #111111;
    --text-light: #ffffff;
  }
  * { margin: 0; padding: 0; box-sizing: border-box; }
  html, body {
    width: 1200px;
    height: 900px;
    overflow: hidden;
    background: var(--canvas-bg);
    font-family: "Open Sans", Arial, sans-serif;
  }
  .canvas {
    position: relative;
    width: 1200px;
    height: 900px;
  }
  .business-card {
    position: absolute;
    width: 556px;
    height: 344px;
    background: var(--card-white);
    box-shadow: 0 6px 18px rgba(0,0,0,0.18);
    overflow: hidden;
  }
  .business-card--curtis { left: 237px; top: 61px; }
  .business-card--nolan  { left: 461px; top: 518px; width: 558px; }

  .card-brand {
    height: 186px;
    display: flex;
    align-items: center;
    justify-content: center;
    gap: 12px;
  }
  .brand-mark {
    width: 18px;
    height: 18px;
    background: var(--ink);
  }
  .brand-name {
    font-weight: 700;
    font-size: 27px;
    letter-spacing: 0.5px;
    color: var(--ink);
    text-transform: uppercase;
  }

  .card-contact {
    position: absolute;
    left: 0; right: 0; bottom: 0;
    height: 158px;
    background: var(--card-black);
    color: var(--text-light);
    padding: 26px 33px 0;
  }
  .contact-name {
    font-weight: 600;
    font-size: 21px;
    text-transform: uppercase;
    margin-bottom: 26px;
    letter-spacing: 0.2px;
  }
  .contact-line {
    display: flex;
    align-items: center;
    gap: 10px;
    font-size: 17px;
    line-height: 25px;
  }
  .contact-icon {
    width: 14px;
    height: 14px;
    flex: none;
    fill: var(--text-light);
  }
</style>
</head>
<body>
<main class="canvas">

  <article class="business-card business-card--curtis">
    <header class="card-brand">
      <span class="brand-mark"></span>
      <span class="brand-name">R &amp; T Summit Construction</span>
    </header>
    <section class="card-contact">
      <h2 class="contact-name">Curtis Hale</h2>
      <p class="contact-line">
        <svg class="contact-icon" viewBox="0 0 24 24" aria-hidden="true"><path d="M6.6 10.8a15.1 15.1 0 0 0 6.6 6.6l2.2-2.2c.3-.3.7-.4 1-.2 1.1.4 2.3.6 3.6.6.6 0 1 .4 1 1V20c0 .6-.4 1-1 1A17 17 0 0 1 3 4c0-.6.4-1 1-1h3.5c.6 0 1 .4 1 1 0 1.3.2 2.5.6 3.6.1.3 0 .7-.2 1z"/></svg>
        512-693-1804
      </p>
      <p class="contact-line">
        <svg class="contact-icon" viewBox="0 0 24 24" aria-hidden="true"><path d="M2 5h20v14H2z M3.5 6.5 12 13l8.5-6.5" fill="none" stroke="#fff" stroke-width="0"/><path d="M2 5h20v2l-10 7L2 7z"/><path d="M2 9l10 7 10-7v10H2z"/></svg>
        curtis@rtsummitconstruction.com
      </p>
    </section>
  </article>

  <article class="business-card business-card--nolan">
    <header class="card-brand">
      <span class="brand-mark"></span>
      <span class="brand-name">R &amp; T Summit Construction</span>
    </header>
    <section class="card-contact">
      <h2 class="contact-name">Nolan Pritchett</h2>
      <p class="contact-line">
        <svg class="contact-icon" viewBox="0 0 24 24" aria-hidden="true"><path d="M6.6 10.8a15.1 15.1 0 0 0 6.6 6.6l2.2-2.2c.3-.3.7-.4 1-.2 1.1.4 2.3.6 3.6.6.6 0 1 .4 1 1V20c0 .6-.4 1-1 1A17 17 0 0 1 3 4c0-.6.4-1 1-1h3.5c.6 0 1 .4 1 1 0 1.3.2 2.5.6 3.6.1.3 0 .7-.2 1z"/></svg>
        512-804-2271
      </p>
      <p class="contact-line">
        <svg class="contact-icon" viewBox="0 0 24 24" aria-hidden="true"><path d="M2 5h20v2l-10 7L2 7z"/><path d="M2 9l10 7 10-7v10H2z"/></svg>
        nolan@rtsummitconstruction.com
      </p>
    </section>
  </article>

</main>
</body>
</html>
```